50 bday

It's my 50th bday and I need the invitation that we will be send by digital (mail and whatapp). One important aspect is that my bday is on day 2 month 2 of year 22 so this is going to be important things that I want to use it as the main theme as you can see in the attached example

```html
<!DOCTYPE html>
<html lang="en">
<head>
<meta charset="UTF-8">
<title>50th Birthday Invitation</title>
<link href="https://fonts.googleapis.com/css2?family=Quicksand:wght@700&family=Yellowtail&family=Fredoka:wght@600&family=Raleway:wght@400&display=swap" rel="stylesheet">
<style>
  :root {
    --page: #ffffff;
    --gold: #df9f2f;
    --gold-light: #eab347;
    --gold-dark: #c98a22;
    --ink: #111111;
    --band: #000000;
    --band-text: #ffffff;
    --day: #3b8a2b;
    --month: #ad0c0c;
    --year: #1d3a70;
  }
  html, body {
    margin: 0;
    padding: 0;
    width: 1200px;
    height: 1200px;
    overflow: hidden;
    background: var(--page);
  }
  .invitation {
    position: absolute;
    left: 125px;
    top: 283px;
    width: 951px;
    height: 633px;
    background:
      radial-gradient(circle at 25% 30%, var(--gold-light) 0%, transparent 35%),
      radial-gradient(circle at 80% 60%, var(--gold-light) 0%, transparent 30%),
      linear-gradient(160deg, var(--gold-light), var(--gold) 45%, var(--gold-dark));
    overflow: hidden;
  }
  .invitation__lead {
    position: absolute;
    top: 36px;
    width: 100%;
    margin: 0;
    text-align: center;
    font-family: 'Quicksand', sans-serif;
    font-weight: 700;
    font-size: 46px;
    color: var(--ink);
    letter-spacing: 0.5px;
  }
  .invitation__title {
    position: absolute;
    top: 84px;
    width: 100%;
    margin: 0;
    text-align: center;
    font-family: 'Yellowtail', cursive;
    font-weight: 400;
    font-size: 88px;
    color: var(--ink);
    line-height: 1;
  }
  .invitation__title sup {
    font-size: 42px;
    vertical-align: 34px;
  }
  .date-digits {
    position: absolute;
    left: 0;
    top: 0;
    width: 951px;
    height: 633px;
  }
  .date-digits__num {
    font-family: 'Fredoka', sans-serif;
    font-weight: 600;
    font-size: 300px;
  }
  .date-digits__label {
    font-family: 'Raleway', sans-serif;
    font-size: 21px;
    letter-spacing: 1px;
  }
  .is-day { fill: var(--day); }
  .is-month { fill: var(--month); }
  .is-year { fill: var(--year); }
  .invitation__band {
    position: absolute;
    left: 0;
    bottom: 0;
    width: 100%;
    height: 129px;
    background: var(--band);
    display: flex;
    align-items: center;
    justify-content: center;
  }
  .invitation__note {
    margin: 0;
    text-align: center;
    font-family: 'Raleway', sans-serif;
    font-weight: 400;
    font-size: 26.5px;
    line-height: 37px;
    color: var(--band-text);
    letter-spacing: -0.3px;
  }
</style>
</head>
<body>
  <main class="invitation">
    <p class="invitation__lead">Invitation To My</p>
    <h1 class="invitation__title">50<sup>th</sup> Birthday Celebration</h1>

    <svg class="date-digits" viewBox="0 0 951 633" aria-label="Day 2, month 2, year 22">
      <defs>
        <filter id="emboss" x="-10%" y="-10%" width="120%" height="120%">
          <feDropShadow dx="3" dy="4" stdDeviation="3" flood-color="#000" flood-opacity="0.35"/>
        </filter>
      </defs>
      <g filter="url(#emboss)">
        <text class="date-digits__num is-day" x="100" y="433">2</text>
        <text class="date-digits__num is-month" x="293" y="433">2</text>
        <text class="date-digits__num is-year" x="486" y="433">2</text>
        <text class="date-digits__num is-year" x="676" y="433">2</text>
      </g>
      <text class="date-digits__label is-day" transform="translate(133 358) rotate(-52)">DAY</text>
      <text class="date-digits__label is-month" transform="translate(325 375) rotate(-52)">MONTH</text>
      <text class="date-digits__label is-year" transform="translate(523 357) rotate(-52)">YEAR</text>
    </svg>

    <div class="invitation__band">
      <p class="invitation__note">RESERVA DESDE AHORA ESE DÍA EN TU AGENDA PARA<br>JUNTOS COMPARTIR EN LA CELEBRACIÓN DE MIS 50 AÑOS</p>
    </div>
  </main>
</body>
</html>
```